Web Design Project

We are an online tax Continuing education provider. We provide online courses for tax preparers. We want the front end page to be user friendly and for the buyer to know exactly what they are looking at. We want a front end page to look smiliar www.marblequill.com. It should have a similar feel to this one.
Our website address will be www.7382LQ.com
We currently have another website that is www.LedgerNoks.com but we do not want it to look like this. We want a different look but same information.
We have a logo already which is attached. We don't have specific colors in mind for the front page but don't want it to be too busy looking. It should stand out but not too simple either.
Target Market(s)
Tax Preparers. More serious and professional but these folks are usually not tech savy. Simple, easy to use, and functional is key.
Industry/Entity Type
Education
Requirements
Must have
- Use standard HTML & CSS. NO other coding is needed.
We are looking for 5-7 pages including Home page, log in, FAQ.
Please look at our current website www.LedgerNoks.com and also www.marblequill.com

```html
<!DOCTYPE html>
<html lang="en">
<head>
<meta charset="utf-8">
<title>7382LQ – Registration</title>
<link href="https://fonts.googleapis.com/css2?family=Roboto+Condensed:wght@300;400;700&family=PT+Sans:wght@400;700&family=Arimo:wght@400;700&display=swap" rel="stylesheet">
<style>
:root{
  --white:#ffffff;
  --teal:#1f5a70;
  --teal-dark:#19485a;
  --ink:#1d1d1d;
  --label:#333333;
  --hint:#9a9a9a;
  --req:#d0282e;
  --hero-top:#e4e4e4;
  --hero-bottom:#c9c9c9;
  --band:#9c9c9c;
  --band-light:#bdbdbd;
  --feature-band:#d2d2d2;
  --orange-top:#f8b843;
  --orange-bottom:#fdcd6d;
  --orange-text:#3a2a05;
  --form-bg:#e8e8e8;
  --field-border:#d6d6d6;
  --btn-top:#6fb4d8;
  --btn-bottom:#1f6d98;
  --footer:#a3a3a3;
  --footer-text:#ffffff;
  --link:#e7eef3;
}
*{box-sizing:border-box;margin:0;padding:0}
html,body{width:878px;height:1200px;overflow:hidden}
body{position:relative;background:var(--form-bg);font-family:"Arimo",Arial,sans-serif;color:var(--ink)}

/* header */
.site-header{position:absolute;left:0;top:0;width:878px;height:104px;background:var(--white);box-shadow:0 2px 6px rgba(0,0,0,.12);z-index:2}
.brand{position:absolute;left:114px;top:62px;display:flex;align-items:center;gap:6px;font-family:"Roboto Condensed",sans-serif;font-weight:700;font-size:26px;color:var(--teal)}
.brand-dot{width:14px;height:14px;border-radius:50%;background:var(--teal)}
.main-nav a{position:absolute;top:73px;font-family:"PT Sans",sans-serif;font-size:11px;color:var(--ink);text-decoration:none}
.sign-in{position:absolute;left:700px;top:68px;width:68px;height:23px;border-radius:3px;background:linear-gradient(#e0e3e6,#c8ccd0);font-family:"PT Sans",sans-serif;font-size:11px;color:var(--teal);display:flex;align-items:center;justify-content:center;gap:5px}

/* hero */
.hero{position:absolute;left:0;top:104px;width:878px;height:230px;background:linear-gradient(var(--hero-top),var(--hero-bottom))}
.hero-band{position:absolute;left:0;top:334px;width:878px;height:43px;background:linear-gradient(var(--band),var(--band-light))}
.hero-copy{position:absolute;left:109px;top:148px;width:252px;font-family:"Roboto Condensed",sans-serif;color:var(--teal);font-size:15.5px;font-weight:400;line-height:33px;text-transform:uppercase;white-space:nowrap}
.hero-copy strong{font-weight:700;font-size:17px}
.slider-dots{position:absolute;left:110px;top:298px;display:flex;gap:6px}
.slider-dots span{width:9px;height:9px;border-radius:50%;background:#9f9f9f;box-shadow:inset 0 1px 2px rgba(0,0,0,.4)}
.slider-dots span.active{background:var(--white)}
.hero-photo{position:absolute;left:371px;top:142px;width:397px;height:216px;background:var(--white);padding:5px;box-shadow:0 3px 8px rgba(0,0,0,.3)}
.hero-photo .fill{width:100%;height:100%;background:linear-gradient(120deg,#c98a3d,#e1a14c 40%,#8c7a6a 70%,#c07a34)}

/* features */
.features{position:absolute;left:0;top:377px;width:878px;height:131px;background:var(--feature-band)}
.feature{position:absolute;top:15px;width:214px;height:98px;background:linear-gradient(var(--orange-top),var(--orange-bottom));padding:12px 12px}
.feature h3{font-family:"PT Sans",sans-serif;font-weight:400;font-size:12.5px;line-height:21px;color:var(--white);text-transform:uppercase}
.feature p{position:absolute;left:12px;bottom:10px;font-family:"PT Sans",sans-serif;font-size:8.5px;line-height:14px;color:var(--orange-text)}
.feature .badge{position:absolute;right:16px;top:12px}

/* registration */
.reg-head{position:absolute;left:0;top:508px;width:878px;height:54px;background:linear-gradient(#d3d3d3,#e2e2e2)}
.reg-title{position:absolute;left:110px;top:20px;font-size:12.5px;font-weight:400;color:var(--teal)}
.reg-note{position:absolute;left:281px;top:22px;font-size:9.5px;color:var(--label)}
.req{color:var(--req)}
.field-label{position:absolute;left:109px;font-size:9.5px;color:var(--label)}
.field-input{position:absolute;left:213px;width:219px;height:28px;background:var(--white);border:1px solid var(--field-border);box-shadow:inset 0 -3px 0 #f0f0f0}
.field-hint{position:absolute;left:445px;font-size:9.5px;color:var(--hint)}
.register-btn{position:absolute;left:213px;top:1086px;width:219px;height:34px;background:linear-gradient(var(--btn-top),var(--btn-bottom));border:1px solid #1a5a80;color:var(--white);font-size:9.5px;font-weight:700;display:flex;align-items:center;justify-content:center;letter-spacing:.2px}

/* footer */
.site-footer{position:absolute;left:0;top:1162px;width:878px;height:38px;background:var(--footer);font-family:"PT Sans",sans-serif;font-size:8.5px;color:var(--footer-text)}
.site-footer .copy{position:absolute;left:110px;top:14px}
.site-footer .legal{position:absolute;left:365px;top:13px;color:var(--link)}
.site-footer .social{position:absolute;left:648px;top:13px}
.social-dots{position:absolute;left:711px;top:11px;display:flex;gap:5px}
.social-dots span{width:15px;height:15px;border-radius:50%;background:#dcdcdc}
</style>
</head>
<body>

<header class="site-header">
  <div class="brand"><span class="brand-dot"></span>7382LQ</div>
  <nav class="main-nav">
    <a style="left:420px">Home</a>
    <a style="left:490px">Courses</a>
    <a style="left:568px">FAQ</a>
    <a style="left:631px">Contact</a>
  </nav>
  <div class="sign-in">
    <svg width="7" height="9" viewBox="0 0 7 9"><circle cx="3.5" cy="2.2" r="2" fill="#1f5a70"/><path d="M0 9c0-3 1.5-4.3 3.5-4.3S7 6 7 9z" fill="#1f5a70"/></svg>
    Sign In
  </div>
</header>

<section class="hero"></section>
<div class="hero-band"></div>
<div class="hero-copy">
  <strong>Easy-to-understand,</strong><br>
  Affordable continuing education<br>
  At your finger tips
</div>
<div class="slider-dots"><span></span><span></span><span></span><span class="active"></span></div>
<div class="hero-photo"><div class="fill" role="img" aria-label="Photo of a student studying on a laptop in a lecture hall"></div></div>

<section class="features">
  <div class="feature" style="left:110px">
    <h3>NRB Approved<br>Provider</h3>
    <svg class="badge" width="50" height="44"><circle cx="25" cy="22" r="20" fill="#ffffff"/></svg>
    <p>Click here to see our<br>approved provider link at NRB website</p>
  </div>
  <div class="feature" style="left:331px">
    <h3>Certificate of<br>Completion</h3>
    <svg class="badge" width="42" height="34"><rect x="1" y="1" width="40" height="32" fill="#f4f4f4" stroke="#7a7a7a"/><rect x="5" y="5" width="32" height="24" fill="none" stroke="#a9a9a9"/><line x1="10" y1="13" x2="32" y2="13" stroke="#8a8a8a"/><line x1="10" y1="18" x2="26" y2="18" stroke="#8a8a8a"/><circle cx="31" cy="23" r="3" fill="#e9b840"/></svg>
    <p>IMPORTANT! All federal tax return preparers<br>must have a current year PTIN.</p>
  </div>
  <div class="feature" style="left:553px">
    <h3>Professional</h3>
    <svg class="badge" width="48" height="46" style="right:8px"><rect x="4" y="10" width="34" height="32" fill="#f2ecd8" stroke="#8a7a5a" transform="rotate(-12 21 26)"/><path d="M24 40 L36 6 L42 40 Z" fill="#e8b33c" stroke="#8a6a20"/></svg>
    <p>Complete your continuing education<br>requirements now so you can concentrate<br>on servicing your tax clients.</p>
  </div>
</section>

<section class="reg-head">
  <h2 class="reg-title">Registration</h2>
  <p class="reg-note">Fields marked with <span class="req">*</span> are mandatory</p>
</section>

<form>
  <label class="field-label" style="top:582px">First Name<span class="req">*</span></label>
  <div class="field-input" style="top:584px"></div>

  <label class="field-label" style="top:628px">Last Name<span class="req">*</span></label>
  <div class="field-input" style="top:630px"></div>

  <label class="field-label" style="top:674px">Address <span class="req">*</span></label>
  <div class="field-input" style="top:676px"></div>

  <label class="field-label" style="top:720px">City<span class="req">*</span></label>
  <div class="field-input" style="top:722px"></div>

  <label class="field-label" style="top:766px">State<span class="req">*</span></label>
  <div class="field-input" style="top:768px"></div>

  <label class="field-label" style="top:812px">Zip Code<span class="req">*</span></label>
  <div class="field-input" style="top:814px"></div>
  <span class="field-hint" style="top:833px">Ex: 99999-9999 or 99999</span>

  <label class="field-label" style="top:858px">Phone<span class="req">*</span></label>
  <div class="field-input" style="top:860px"></div>
  <span class="field-hint" style="top:880px">Ex: 999-999-9999</span>

  <label class="field-label" style="top:903px">Email Address<span class="req">*</span></label>
  <div class="field-input" style="top:905px"></div>
  <span class="field-hint" style="top:925px">(This will be your User ID during LogIn)</span>

  <label class="field-label" style="top:949px">Verify Email Address<span class="req">*</span></label>
  <div class="field-input" style="top:950px"></div>

  <label class="field-label" style="top:994px">Password<span class="req">*</span></label>
  <div class="field-input" style="top:996px"></div>
  <span class="field-hint" style="top:1013px">(This will be your Password during LogIn)</span>

  <label class="field-label" style="top:1039px">Verify Password<span class="req">*</span></label>
  <div class="field-input" style="top:1041px"></div>

  <div class="register-btn">REGISTER YOUR ACCOUNT NOW</div>
</form>

<footer class="site-footer">
  <span class="copy">Copyright © 2012. All Rights Reserved</span>
  <span class="legal">Terms &amp; Condition &nbsp;&nbsp;|&nbsp;&nbsp; Privacy Policy</span>
  <span class="social">Social Media</span>
  <div class="social-dots"><span></span><span></span><span></span></div>
</footer>

</body>
</html>
```